Technology management company looking for a new website with a professional look

Brennick IT is a recently re-branded technology management company that is looking for a website design to match its personalized approach and friendly culture.

We would like to see a specialized, but related, page style for each of our main service offerings of:

• Commercial IT Support (This is our primary focus)
• Commercial Phone Systems (We partner with http://www.voxtrell.com/ for our phone systems)
• Point of Sale Systems (We partner with http://www.tillmora.com/ for our POS systems.
• Web Design
• Hollow Pine Computers (Our residential computer service offering, branded as Hollow Pine Computers)

The Hollow Pine Computers page should be build upon the Hollow Pine Computers logo, the other four pages should be branded as Brennick IT.

These five separate pages should have subtle, yet clearly defined links to one another. They should also each have a Home, Products, Service, and Company in the menu.

The website should have a clean design with professional appeal, but not appear too sterile or uninviting. It needs to have a simple, easy to navigate menu interface along the top. We would also like the site to be mobile friendly.

It should also allow us to easily tie in links to our social media pages (Facebook, LinkedIn, Twitter and Google+) and provide easy access to our contact information from each page.

This is a link to our old website www.hollowpinecomputers.com

We don't currently have copy available. The text and menu design should be easily editable and expandable so we can use the design to fit our copy.

In general we are looking for a concept we can modify to fit our needs.

We need this design to be available with layers in a .psd format.

Target Market(s)

Small to mid-size businesses.

Industry/Entity Type

Information Technology

Number of Pages Required

5+ page

Font styles to use
Sans Serif

Requirements
Must have
• Mobile Friendly
• Professional Type Face
• Unity between all pages
• .PSD Format
Nice to have
• Themed with our logo
Should not have
• Bubbly unprofessional typeface. No comic sans.

```html
<!DOCTYPE html>
<html lang="en">
<head>
<meta charset="utf-8">
<title>Brennick IT</title>
<link rel="stylesheet" href="https://fonts.googleapis.com/css2?family=Open+Sans:ital,wght@0,400;0,600;0,700;1,400&display=swap">
<style>
:root{
  --orange:#ef5a1c;
  --navy:#1e4a8a;
  --title:#3b4a5a;
  --text:#777d84;
  --light:#f3f4f5;
  --rule:#dcdfe2;
  --footer:#2b2f33;
  --footer-bottom:#222528;
  --footer-text:#a3a8ad;
  --white:#ffffff;
}
*{box-sizing:border-box;margin:0;padding:0}
html,body{width:1200px;height:2236px;overflow:hidden;background:var(--white)}
body{font-family:"Open Sans",Arial,sans-serif;color:var(--text);font-size:13px}

.site-header{height:120px;display:flex;align-items:center;justify-content:space-between;padding:0 80px 0 90px}
.brand{display:flex;align-items:center;gap:12px;font-size:40px;font-weight:700;color:var(--title)}
.brand-mark{width:34px;height:34px;border-radius:50%;background:var(--orange)}
.header-contacts{display:flex;gap:60px}
.contact-item{display:flex;align-items:center;gap:12px;font-size:12px;line-height:1.35}
.contact-item strong{display:block;color:var(--orange);font-size:14px}
.contact-icon{width:32px;height:32px;border:1px solid var(--rule);border-radius:50%;display:flex;align-items:center;justify-content:center}

.main-nav{height:36px;background:var(--orange);display:flex;justify-content:center}
.main-nav a{width:138px;text-align:center;color:var(--white);font-size:12px;font-weight:600;line-height:36px;letter-spacing:.5px}
.main-nav a.active{background:var(--navy)}

.hero{position:relative;height:584px;overflow:hidden}
.hero-photo{position:absolute;inset:0;background:linear-gradient(100deg,#6e849b 0%,#9eb0c1 40%,#7f93a7 70%,#a9b7c4 100%)}
.hero-device{position:absolute;left:160px;top:124px;width:330px;height:280px;background:linear-gradient(160deg,#e7e9eb,#bfc5cb);border-radius:6px}
.hero-copy{position:absolute;left:540px;top:170px;color:var(--white)}
.hero-copy h1{font-size:46px;font-weight:400;line-height:1.2;white-space:nowrap;text-shadow:0 1px 3px rgba(0,0,0,.25)}
.hero-badge{display:inline-block;width:46px;height:46px;border-radius:50%;background:rgba(255,255,255,.85);vertical-align:middle;margin-left:34px}
.btn-outline{display:inline-block;margin-top:44px;border:2px solid var(--white);color:var(--white);font-size:12px;font-weight:600;padding:11px 18px;letter-spacing:.5px}

.section-title{text-align:center;color:var(--title);font-size:28px;font-weight:700;letter-spacing:.5px}
.section-sub{text-align:center;font-size:11px;margin-top:10px;letter-spacing:.3px}

.services{padding-top:40px;height:390px;position:relative}
.service-cards{display:flex;gap:20px;justify-content:center;margin-top:30px}
.service-card{width:236px;background:var(--white);box-shadow:0 1px 4px rgba(0,0,0,.12)}
.service-photo{height:130px;position:relative}
.service-icon{position:absolute;left:50%;bottom:-22px;transform:translateX(-50%);width:44px;height:44px;border-radius:50%;background:var(--orange);border:3px solid var(--white)}
.service-card h3{text-align:center;color:var(--title);font-size:14px;font-weight:600;margin-top:32px}
.service-card p{text-align:center;font-size:10.5px;line-height:1.5;padding:8px 18px 16px}
.slider-arrow{position:absolute;top:220px;width:20px;height:50px;background:var(--light);display:flex;align-items:center;justify-content:center}
.slider-arrow.left{left:62px}.slider-arrow.right{right:62px}

.divider{display:flex;align-items:center;justify-content:center;gap:14px;height:20px}
.divider span{width:450px;height:1px;background:var(--rule)}
.divider i{width:24px;height:22px;display:block;background:radial-gradient(circle,#9aa3ac 40%,transparent 42%)}

.welcome{padding-top:30px;height:420px}
.welcome-body{display:flex;gap:40px;margin:40px 0 0 130px}
.welcome-photo{width:300px;height:240px;background:linear-gradient(150deg,#c3ccd6,#7c8896 60%,#3e4954)}
.welcome-text{width:620px;font-size:11px;line-height:1.7;padding-top:20px}
.welcome-text h4{font-size:11px;font-weight:600;color:var(--title);margin-bottom:14px}
.btn-solid{display:inline-block;margin-top:22px;background:var(--orange);color:var(--white);font-size:11px;font-weight:600;padding:10px 18px}

.testimonials{padding-top:30px;height:290px}
.quote{width:800px;margin:28px auto 0;font-style:italic;font-size:13px;line-height:1.6;color:var(--navy)}
.quote-author{text-align:center;font-size:12px;margin-top:20px}
.quote-author b{color:var(--title)}
.dots{display:flex;justify-content:center;gap:7px;margin-top:18px}
.dots i{width:7px;height:7px;border-radius:50%;background:var(--rule)}
.dots i.on{background:var(--orange)}

.partners{height:100px;background:var(--light);display:flex;align-items:center;justify-content:center;gap:110px;border-top:1px solid var(--rule)}
.partner{display:flex;align-items:center;gap:8px;font-size:18px;font-weight:700;color:var(--title)}
.partner i{width:16px;height:16px;background:var(--orange);display:block}

.site-footer{background:var(--footer);height:200px;display:flex;gap:30px;padding:34px 0 0 100px}
.footer-col{width:180px}
.footer-col h5{color:var(--white);font-size:13px;font-weight:600;margin-bottom:14px}
.footer-col li{list-style:none;font-size:11px;color:var(--footer-text);line-height:2}
.newsletter p{font-size:11px;color:var(--footer-text);line-height:1.6;width:170px}
.newsletter-field{margin-top:12px;width:180px;height:28px;background:#3a3f44;border:1px solid #474c51}
.footer-bottom{background:var(--footer-bottom);height:46px;display:flex;align-items:center;justify-content:space-between;padding:0 100px;font-size:11px;color:var(--footer-text)}
.social{display:flex;align-items:center;gap:6px}
.social i{width:20px;height:20px;border-radius:50%;background:#3d7ec9;display:block}
</style>
</head>
<body>

<header class="site-header">
  <div class="brand"><span class="brand-mark"></span>Brennick IT</div>
  <div class="header-contacts">
    <div class="contact-item">
      <span class="contact-icon"><svg width="12" height="12" viewBox="0 0 12 12"><path d="M2 2h8v8H2z" fill="none" stroke="#ef5a1c" stroke-width="1.2"/><path d="M4 6h4M6 4v4" stroke="#ef5a1c" stroke-width="1.2"/></svg></span>
      <div>Need support? Ask us<strong>GET A FREE QUOTE</strong></div>
    </div>
    <div class="contact-item">
      <span class="contact-icon"><svg width="12" height="12" viewBox="0 0 12 12"><path d="M3 1l2 2.5-1.2 1.3a6 6 0 0 0 3.4 3.4L8.5 7 11 9l-1.2 1.8C5.5 10.5 1.5 6.5 1.2 2.2z" fill="#ef5a1c"/></svg></span>
      <div>Call us today<strong>(555) 014-2290</strong></div>
    </div>
  </div>
</header>

<nav class="main-nav">
  <a class="active">HOME</a><a>SERVICES</a><a>PROJECTS</a><a>ABOUT</a><a>NEWS</a><a>FAQ</a><a>CONTACTS</a>
</nav>

<section class="hero">
  <div class="hero-photo" role="img" aria-label="City office towers photographed from street level"></div>
  <div class="hero-device" role="img" aria-label="Laptop showing an IT services web page"></div>
  <div class="hero-copy">
    <h1>We Are Provide IT Services<br>Company..!<span class="hero-badge" role="img" aria-label="Gear emblem"></span></h1>
    <a class="btn-outline">VIEW MORE DETAILS</a>
  </div>
</section>

<section class="services">
  <h2 class="section-title">OUR SERVICES</h2>
  <p class="section-sub">SIMPLY DUMMY TEXT OF THE PRINTING AND TYPESETTING INDUSTRY. LOREM IPSUM</p>
  <div class="slider-arrow left"><svg width="8" height="14"><path d="M7 1L1 7l6 6" fill="none" stroke="#999" stroke-width="1.5"/></svg></div>
  <div class="slider-arrow right"><svg width="8" height="14"><path d="M1 1l6 6-6 6" fill="none" stroke="#999" stroke-width="1.5"/></svg></div>
  <div class="service-cards">
    <article class="service-card">
      <div class="service-photo" role="img" aria-label="Technician at a desk giving IT support" style="background:linear-gradient(150deg,#b8c4d2,#5e7189)"><span class="service-icon"></span></div>
      <h3>Commercial IT Support</h3>
      <p>Reliable help desk and network care that keeps your office running every single day.</p>
    </article>
    <article class="service-card">
      <div class="service-photo" role="img" aria-label="Office desk phone system" style="background:linear-gradient(150deg,#d7dadd,#8d959d)"><span class="service-icon"></span></div>
      <h3>Commercial Phone Systems</h3>
      <p>Modern business phone lines with clear calls, voicemail and easy transfer between desks.</p>
    </article>
    <article class="service-card">
      <div class="service-photo" role="img" aria-label="Retail checkout terminal" style="background:linear-gradient(150deg,#c9ced4,#6c7782)"><span class="service-icon"></span></div>
      <h3>Point of Sale Systems</h3>
      <p>Fast checkout terminals, card readers and inventory tools built for busy shops.</p>
    </article>
    <article class="service-card">
      <div class="service-photo" role="img" aria-label="Web design sketch on a laptop screen" style="background:linear-gradient(150deg,#e2e4e6,#9aa3ac)"><span class="service-icon"></span></div>
      <h3>Web Design</h3>
      <p>Clean, mobile friendly websites that present your business well and bring in leads.</p>
    </article>
  </div>
</section>

<div class="divider"><span></span><i role="img" aria-label="Small gear divider"></i><span></span></div>

<section class="welcome">
  <h2 class="section-title">WELCOME TO BRENNICK IT</h2>
  <div class="welcome-body">
    <div class="welcome-photo" role="img" aria-label="Business handshake in a modern office"></div>
    <div class="welcome-text">
      <h4>SIMPLY DUMMY TEXT OF THE PRINTING AND TYPESETTING INDUSTRY. LOREM IPSUM</h4>
      <p>Brennick IT is a friendly technology partner for small and mid-size businesses. We look after your computers, networks, phones and point of sale so your team can focus on its work. Our technicians know your setup by name, answer quickly and plan ahead so problems are fixed before they slow you down. From a single office to several locations, we bring the same careful, personal service to every client, with clear advice, fair pricing and support you can count on.</p>
      <a class="btn-solid">READ MORE</a>
    </div>
  </div>
</section>

<div class="divider"><span></span><i role="img" aria-label="Small gear divider"></i><span></span></div>

<section class="testimonials">
  <h2 class="section-title">CLIENT TESTIMONIALS</h2>
  <p class="quote">Lorem Ipsum is simply dummy text of the printing and typesetting industry. Lorem Ipsum has been the industry's standard dummy text ever since the 1500s, when an unknown printer took a galley of type and scrambled it to make a type specimen book.</p>
  <p class="quote-author"><b>Robert Market</b> | Company Name</p>
  <div class="dots"><i class="on"></i><i></i><i></i><i></i><i></i></div>
</section>

<div class="partners">
  <div class="partner"><i></i>Voxtrell</div>
  <div class="partner"><i></i>Tillmora</div>
  <div class="partner"><i></i>Hollow Pine Computers</div>
  <div class="partner"><i></i>Kestrel Data</div>
</div>

<footer>
  <div class="site-footer">
    <div class="footer-col"><h5>Company Info</h5><ul><li>Our Mission</li><li>Milestones</li><li>Employment</li></ul></div>
    <div class="footer-col"><h5>Spotlight</h5><ul><li>Press Center</li><li>Success Stories</li><li>The Lab Archive</li></ul></div>
    <div class="footer-col"><h5>Software</h5><ul><li>IT Cloud Solutions</li><li>Managed Backup</li><li>Network Monitoring</li></ul></div>
    <div class="footer-col"><h5>Support</h5><ul><li>Repair Request</li><li>Help Desk Portal</li><li>Knowledge Base</li></ul></div>
    <div class="footer-col newsletter"><h5>Newsletter</h5><p>Sign up for tips and news from our team.</p><div class="newsletter-field"></div></div>
  </div>
  <div class="footer-bottom">
    <span>© 2024 Brennick IT. All Rights Reserved.</span>
    <div class="social">Connect With Us <i></i><i></i><i></i><i></i></div>
  </div>
</footer>

</body>
</html>
```